Business Card Design for Marketing Firm

Looking for business card design for higher end marketing firm. Clean but impressionable/trendy. We are a marketing firm that represents manufacturers in the foodservice equipment and supply industry. Our customers are end users such has hotels, restaurants, country clubs, convention centers and casinos as well as distributors of restaurants supplies and equipment, and manufacturers of foodservice equipment and supplies.
Target Market(s)
Hotels, Restaurants, Supply & Equipment Distributors, Foodservice Manufacturers
Industry/Entity Type
Foodservice/Hospitality
Contact Information for Business Card
Name, Title, Contact Number, Email, Website, Social Media, Address
Requirements
Must have
- Clean & Simple but Serious and Impressionable

```html
<!DOCTYPE html>
<html lang="en">
<head>
<meta charset="utf-8">
<title>Meridian Table Reps – Business Card</title>
<link href="https://fonts.googleapis.com/css2?family=Cinzel:wght@700&family=Arimo:wght@400&display=swap" rel="stylesheet">
<style>
  :root {
    --bg: #d4d7d9;
    --paper: #fbfbfa;
    --navy: #1d1f5c;
    --grey: #5d5f66;
    --rule: #6e70a4;
  }
  * { box-sizing: border-box; margin: 0; padding: 0; }
  html, body { width: 1200px; height: 829px; overflow: hidden; }
  body {
    background: var(--bg);
    position: relative;
    font-family: "Arimo", Arial, sans-serif;
  }
  .card {
    position: absolute;
    top: 250px;
    width: 525px;
    height: 300px;
    background: var(--paper);
    border-bottom: 4px solid var(--navy);
    box-shadow: 0 10px 24px rgba(0,0,0,0.16);
  }
  .card--contact { left: 50px; }
  .card--brand { left: 625px; }

  .person {
    position: absolute;
    left: 40px;
    top: 42px;
  }
  .person__name {
    font-family: "Cinzel", Georgia, serif;
    font-weight: 700;
    font-size: 21px;
    color: var(--navy);
    letter-spacing: 0.5px;
  }
  .person__title {
    font-size: 13px;
    color: var(--grey);
    margin-top: 2px;
  }
  .rule {
    position: absolute;
    height: 1px;
    background: var(--rule);
  }
  .rule--contact { left: 40px; right: 40px; top: 100px; }

  .contact-list {
    position: absolute;
    left: 40px;
    top: 116px;
    list-style: none;
  }
  .contact-list li {
    display: flex;
    align-items: center;
    gap: 7px;
    font-size: 13px;
    line-height: 20px;
    color: var(--grey);
  }
  .contact-list svg { width: 11px; height: 11px; fill: var(--navy); flex: none; }

  .wordmark {
    font-family: "Cinzel", Georgia, serif;
    font-weight: 700;
    color: var(--navy);
    text-align: right;
    line-height: 1.05;
  }
  .card--contact .wordmark {
    position: absolute;
    right: 40px;
    top: 150px;
    font-size: 22px;
  }
  .card--brand .wordmark {
    position: absolute;
    left: 0; right: 0;
    top: 108px;
    text-align: center;
    font-size: 34px;
  }
  .address {
    position: absolute;
    right: 40px;
    bottom: 30px;
    font-size: 13px;
    line-height: 18px;
    color: var(--grey);
  }
</style>
</head>
<body>
  <section class="card card--contact" aria-label="Business card, contact side">
    <div class="person">
      <h1 class="person__name">DANIEL BROOKS</h1>
      <p class="person__title">CEO/Founder</p>
    </div>
    <div class="rule rule--contact"></div>
    <ul class="contact-list">
      <li><svg viewBox="0 0 12 12"><path d="M3 1 L5 3.5 L4 5 Q5.5 7 7 8 L8.5 7 L11 9 L10 11 Q5 11 1 4 Z"/></svg>555-014-2290</li>
      <li><svg viewBox="0 0 12 12"><path d="M1 2.5 H11 V9.5 H1 Z M1.5 3 L6 6.5 L10.5 3" fill="none" stroke="#1d1f5c" stroke-width="1.2"/></svg>hello@meridiantablereps.com</li>
      <li><svg viewBox="0 0 12 12"><circle cx="6" cy="6" r="5"/></svg>www.meridiantablereps.com</li>
      <li><svg viewBox="0 0 12 12"><circle cx="6" cy="6" r="5"/></svg>@meridiantablereps</li>
    </ul>
    <div class="wordmark">MERIDIAN TABLE<br>REPS</div>
    <p class="address">48 Harbor Lane, Suite 210<br>Eastfield, CA 90215</p>
  </section>

  <section class="card card--brand" aria-label="Business card, brand side">
    <div class="wordmark">MERIDIAN TABLE<br>REPS</div>
  </section>
</body>
</html>
```